BANNER PUBBLICITARIO FACEBOOK

Advertise our services via facebook.
We are a medical center of diagnostic imaging, perform MRI, CT, ultrasound and specialist visits. I want to advertise our center through Facebook trying to get the knowledge of our center to as many people as possible. our target audience are people from 18 to 80 years old.
I want to highlight our contact details, our address and our website www. ponteval.it. All contact information can be found on our website
Updates

Target Market(s)

my target market are people from 18 to 80 years old who have to perform diagnostic tests such as magnetic resonance imaging tac ultrasound etc

Colors
0054AA
0677BA
7BADD7
CADEEF
E8F1F8
0094D4
00A9DD
6FCCEA
C7EBF8
E9F6FB
00AB8E
00BBA5
67D7C9
C6EFE9
E9F9F6

Requirements
Must have
• my project should be impactful and attractive. When the user sees my post he must be attracted
Nice to have
• I would like to highlight our diagnostic machines, so that the customers understand immediately what we are doing. As indicated on our website www.ponteval.it

```html
<!DOCTYPE html>
<html lang="en">
<head>
<meta charset="UTF-8">
<title>Ponteval Diagnostic Center</title>
<link href="https://fonts.googleapis.com/css2?family=Poppins:wght@400;500;600;700;800&display=swap" rel="stylesheet">
<style>
  :root {
    --navy: #0054AA;
    --blue: #0677BA;
    --sky: #0094D4;
    --cyan: #6FCCEA;
    --ice: #E8F1F8;
    --teal: #00AB8E;
    --ink: #1b1d21;
    --white: #ffffff;
  }
  html, body {
    margin: 0;
    padding: 0;
    width: 1200px;
    height: 1200px;
    overflow: hidden;
  }
  .banner {
    position: relative;
    width: 1200px;
    height: 1200px;
    overflow: hidden;
    background: linear-gradient(135deg, #ffffff 0%, #f4f7fa 60%, #eef2f6 100%);
    font-family: "Poppins", sans-serif;
    color: var(--ink);
  }
  .swoosh { position: absolute; inset: 0; }
  .brand {
    position: absolute;
    left: 68px;
    top: 52px;
    display: flex;
    align-items: center;
    gap: 16px;
    font-weight: 600;
    font-size: 76px;
    line-height: 1;
    color: var(--blue);
    letter-spacing: -1px;
  }
  .brand-dot {
    width: 22px;
    height: 22px;
    border-radius: 50%;
    background: var(--teal);
  }
  .headline {
    position: absolute;
    left: 66px;
    top: 206px;
    margin: 0;
    font-weight: 800;
    font-size: 116px;
    line-height: 1.02;
    letter-spacing: 1px;
  }
  .headline .line-blue { color: var(--navy); display: block; }
  .headline .line-dark { color: var(--ink); display: block; }
  .tagline {
    position: absolute;
    left: 74px;
    top: 462px;
    margin: 0;
    font-size: 40px;
    line-height: 1.3;
    letter-spacing: -0.5px;
  }
  .tagline strong { font-weight: 700; display: block; }
  .tagline span { font-weight: 400; display: block; }
  .services {
    position: absolute;
    left: 68px;
    top: 596px;
    margin: 0;
    padding: 0;
    list-style: none;
    font-size: 34px;
    line-height: 1.55;
    font-weight: 400;
    letter-spacing: 0.3px;
  }
  .services li {
    display: flex;
    align-items: flex-start;
    gap: 22px;
    margin-bottom: 6px;
  }
  .services li.gap-after { margin-bottom: 16px; }
  .services svg { flex: none; margin-top: 10px; }
  .contact {
    position: absolute;
    left: 74px;
    top: 914px;
    display: flex;
    align-items: center;
    gap: 36px;
  }
  .contact-label {
    font-weight: 700;
    font-size: 34px;
    color: var(--teal);
    line-height: 1.2;
  }
  .contact-phone {
    font-size: 34px;
    line-height: 1.2;
  }
  .info-row {
    position: absolute;
    left: 72px;
    display: flex;
    align-items: flex-start;
    gap: 22px;
    font-size: 29px;
  }
  .hours { top: 1036px; font-weight: 700; }
  .address { top: 1094px; line-height: 1.45; }
  .address strong { font-weight: 700; display: block; }
  .email {
    position: absolute;
    left: 810px;
    top: 1130px;
    display: flex;
    align-items: center;
    gap: 20px;
    color: var(--white);
    font-size: 31px;
  }
  .equipment-photo {
    position: absolute;
    left: 578px;
    top: 345px;
    width: 688px;
    height: 688px;
    border-radius: 50%;
    box-sizing: border-box;
    border: 12px solid var(--white);
    background: radial-gradient(circle at 45% 50%, #f6f8fa 0%, #e4e9ee 45%, #c9d3dc 75%, #b7c6d3 100%);
  }
</style>
</head>
<body>
<main class="banner">
  <svg class="swoosh" width="1200" height="1200" viewBox="0 0 1200 1200" aria-hidden="true">
    <path d="M480 0 H778 C960 110 1110 270 1200 440 V600 C1100 380 860 120 480 0 Z" fill="#6FCCEA"/>
    <path d="M778 0 H1000 C1070 90 1130 200 1200 330 V440 C1110 270 960 110 778 0 Z" fill="#0677BA"/>
    <path d="M1000 0 H1200 V330 C1130 200 1070 90 1000 0 Z" fill="#0054AA"/>
    <path d="M1200 300 V1200 H1100 V300 Z" fill="#0054AA"/>
    <path d="M620 1200 C700 1120 800 1060 900 1020 L1200 980 V1200 Z" fill="#0094D4"/>
    <path d="M700 1200 C820 1110 960 1060 1200 1040 V1200 Z" fill="#0677BA"/>
    <path d="M1000 1200 C1060 1140 1130 1100 1200 1080 V1200 Z" fill="#0054AA"/>
  </svg>

  <div class="brand"><span>Ponteval</span><span class="brand-dot"></span></div>

  <h1 class="headline">
    <span class="line-blue">DIAGNOSTIC</span>
    <span class="line-dark">CENTER</span>
  </h1>

  <p class="tagline">
    <strong>PIONEERS IN</strong>
    <span>DIAGNOSTIC PRACTICE</span>
  </p>

  <ul class="services">
    <li><svg width="36" height="36" viewBox="0 0 36 36"><circle cx="17" cy="19" r="14" fill="none" stroke="#00AB8E" stroke-width="4"/><path d="M10 18 L16 24 L32 5" fill="none" stroke="#00AB8E" stroke-width="5" stroke-linecap="round" stroke-linejoin="round"/></svg><span>Magnetic Resonance</span></li>
    <li class="gap-after"><svg width="36" height="36" viewBox="0 0 36 36"><circle cx="17" cy="19" r="14" fill="none" stroke="#00AB8E" stroke-width="4"/><path d="M10 18 L16 24 L32 5" fill="none" stroke="#00AB8E" stroke-width="5" stroke-linecap="round" stroke-linejoin="round"/></svg><span>Tac 128 Slice</span></li>
    <li><svg width="36" height="36" viewBox="0 0 36 36"><circle cx="17" cy="19" r="14" fill="none" stroke="#00AB8E" stroke-width="4"/><path d="M10 18 L16 24 L32 5" fill="none" stroke="#00AB8E" stroke-width="5" stroke-linecap="round" stroke-linejoin="round"/></svg><span>Ultrasound Vascular<br>Ecocolodoppler</span></li>
    <li><svg width="36" height="36" viewBox="0 0 36 36"><circle cx="17" cy="19" r="14" fill="none" stroke="#00AB8E" stroke-width="4"/><path d="M10 18 L16 24 L32 5" fill="none" stroke="#00AB8E" stroke-width="5" stroke-linecap="round" stroke-linejoin="round"/></svg><span>Traditional Radiology</span></li>
  </ul>

  <div class="contact">
    <svg width="74" height="86" viewBox="0 0 74 86" aria-hidden="true">
      <rect x="6" y="0" width="68" height="86" rx="6" fill="#00AB8E"/>
      <rect x="0" y="14" width="12" height="8" rx="3" fill="#00AB8E"/>
      <rect x="0" y="39" width="12" height="8" rx="3" fill="#00AB8E"/>
      <rect x="0" y="64" width="12" height="8" rx="3" fill="#00AB8E"/>
      <circle cx="40" cy="32" r="12" fill="#fff"/>
      <path d="M20 68 C20 52 60 52 60 68 Z" fill="#fff"/>
    </svg>
    <div>
      <div class="contact-label">CONTACT US</div>
      <div class="contact-phone">0549-904378</div>
    </div>
  </div>

  <div class="info-row hours">
    <svg width="40" height="40" viewBox="0 0 40 40" aria-hidden="true"><circle cx="20" cy="20" r="16" fill="none" stroke="#00AB8E" stroke-width="4"/><path d="M20 10 V20 L27 25" fill="none" stroke="#00AB8E" stroke-width="4" stroke-linecap="round"/></svg>
    <span>Mon-Fri 8:00-19:00</span>
  </div>

  <div class="info-row address">
    <svg width="36" height="48" viewBox="0 0 36 48" aria-hidden="true"><path d="M18 0 C8 0 0 8 0 18 C0 30 18 48 18 48 C18 48 36 30 36 18 C36 8 28 0 18 0 Z" fill="#00AB8E"/><circle cx="18" cy="17" r="7" fill="#fff"/></svg>
    <span><strong>Cortina Road, 18</strong>47893, Borgo Lieto, RSM</span>
  </div>

  <div class="equipment-photo" role="img" aria-label="Photo of a white MRI scanner with a light blue patient table"></div>

  <div class="email">
    <svg width="46" height="34" viewBox="0 0 46 34" aria-hidden="true"><rect x="2" y="2" width="42" height="30" rx="2" fill="none" stroke="#fff" stroke-width="3"/><path d="M2 3 L23 20 L44 3 M2 31 L17 16 M44 31 L29 16" fill="none" stroke="#fff" stroke-width="3"/></svg>
    <span>info@ponteval.it</span>
  </div>
</main>
</body>
</html>
```